Funny Images+Videos Mobile App

Jolvo is a entertainment app to watch funny media items(images and videos).

UI Design for a mobile app (Android & iOS) with the following requirements:

- List funny pics and videos in a simple minimalistic interface. All items are listed in just one vertical scrollable view (like pinwharf feed appearance). Each item will display a title (at the top/start of the image or video since it sometimes is the introduction or even part of the joke), number of comments, number of points, and 4 buttons (upvote,downvote,comment and share). Upvote/downvote button can be hidden if the item has been already voted.

- Sign up and log in/out to be able to comment and vote.

The resources needed are:

- Vectorial App Icon
- Vectorial Launch Image icon
- Vectorial Featured (1024x500 px) and Promo banners (180x120 px) for Trellis Shop

The app need at least the following screens:
- Vertical scrollable feed as described above. Videos will also include a play button. After tapping this button it will show a progress loading bar as videos is downloaded from Internet (a pie progress view will be interesting).
- Log in screen (Pinwharf, K+, Email+Pass)
- Sign up screen (Pinwharf and (ask username for Jolvo after validating Pinwharf account), Kestrel+ and (ask username after validating Kestrel+ account) , Email+username+Pass)
- Password recovery and password change screens
- Settings screen. it will include the following options:
- Clear cache
- Change Pass
- Logout
- Send us feedback
- Comments screen. It will list all comments posted for a item and it will let the user upvote/downvote comments and post a new comment.
- My Account. It will display username, profile pic and a list with your latest upvotes pics, and other list with your latest comments.
- Miscellaneous: Other features required:
+ Layout for loading progress: an horizontal progress bar and a pie progress bar.
+ Errors: A proper layout to inform about errors (for example: fail to load item, fail to load lists, fail to log in) messages in empty lists and so on.
+ For the UI elements like buttons, checkboxes, switch (on/off) is required the following status: normal, pressed, disabled and focused.

Nice to have features:

- The design should focus in a base color, a main color (for elements like titles and details) and can use (but not abuse) additional color for small details (like icons or icon parts)

- Feel free to add things and be creative, il will be positively considered.
- iOS and Android design can be slightly different.
- iOS design has to accomplish UI design basics for iOS 7 and xOS Visual Layout Principles.
- First version of the app will not include Log In/My Account and Comments Screen and this requirement should be taken into consideration to design the app.
Similar apps: Please have a look at the following apps to understand the idea:
Chortly,4QUIP

Should not have:
- The app should not have garish or poorly contrasted colors and icons.
- Since the images usually have text inside, floating elements and controls should be avoided further than, for example, a small date label in one corner.

Target Market:
Focused but not limited to young (18-30 y.o.) Internet users.

```html
<!DOCTYPE html>
<html lang="en">
<head>
<meta charset="utf-8">
<title>Jolvo – Feed</title>
<link rel="stylesheet" href="https://fonts.googleapis.com/css2?family=Anton&family=Montserrat:wght@400;500;600;700&display=swap">
<style>
  :root {
    --page-bg: #e6e9ec;
    --status-navy: #0f3a6b;
    --header-blue: #95c5ee;
    --tab-active: #2f5e90;
    --title-blue: #4a78a6;
    --meta-grey: #8a8f95;
    --divider: #e4e6e8;
    --frame-grey: #9a9ea3;
    --icon-grey: #b9bdc1;
    --white: #ffffff;
  }
  * { box-sizing: border-box; margin: 0; padding: 0; }
  html, body {
    width: 934px; height: 1200px; overflow: hidden;
    background: var(--page-bg);
    font-family: "Montserrat", sans-serif;
  }
  .screen {
    position: absolute; left: 129px; top: 0;
    width: 676px; height: 1200px;
    background: var(--white); overflow: hidden;
  }
  .status-bar {
    position: absolute; left: 0; top: 0; width: 100%; height: 43px;
    background: var(--status-navy); color: var(--white);
    font-size: 22px; font-weight: 500;
    display: flex; align-items: center; justify-content: space-between;
    padding: 0 14px;
  }
  .status-left, .status-right { display: flex; align-items: center; gap: 8px; width: 200px; }
  .status-right { justify-content: flex-end; }
  .signal { display: flex; gap: 3px; }
  .signal i { width: 10px; height: 10px; border-radius: 50%; background: var(--white); display: block; }
  .battery { width: 48px; height: 20px; border: 2px solid var(--white); border-radius: 4px; padding: 2px; position: relative; }
  .battery::before { content: ""; display: block; width: 100%; height: 100%; background: var(--white); border-radius: 1px; }
  .battery::after { content: ""; position: absolute; right: -6px; top: 5px; width: 3px; height: 7px; background: var(--white); border-radius: 0 2px 2px 0; }
  .app-header {
    position: absolute; left: 0; top: 43px; width: 100%; height: 91px;
    background: var(--header-blue);
  }
  .app-header .menu { position: absolute; left: 20px; top: 27px; }
  .app-header .brand {
    position: absolute; left: 0; right: 0; top: 22px; text-align: center;
    color: var(--white); font-size: 42px; font-weight: 700; letter-spacing: 1px;
  }
  .app-header .actions { position: absolute; right: 20px; top: 26px; display: flex; gap: 14px; }
  .feed { position: absolute; left: 22px; top: 134px; width: 635px; }
  .post-title {
    border-top: 1px solid var(--divider); border-bottom: 1px solid var(--divider);
    color: var(--title-blue); font-size: 22px; font-weight: 500;
    height: 60px; line-height: 58px; margin-top: 12px;
  }
  .post-meta {
    display: flex; justify-content: space-between; align-items: center;
    height: 50px; font-size: 15px; color: var(--meta-grey);
  }
  .post-meta .comments { color: var(--title-blue); }
  .media {
    position: relative; width: 635px; border: 6px solid var(--frame-grey);
  }
  .media-photo {
    height: 456px;
    background: linear-gradient(180deg, #6c7f8f 0%, #8fa2ae 35%, #c3cccf 55%, #8c9194 75%, #6f7174 100%);
  }
  .meme-caption {
    position: absolute; left: 0; right: 0; text-align: center;
    font-family: "Anton", sans-serif; font-size: 48px; color: var(--white);
    letter-spacing: 0.5px;
    text-shadow: -2px -2px 0 #000, 2px -2px 0 #000, -2px 2px 0 #000, 2px 2px 0 #000;
  }
  .meme-caption.top { top: 8px; }
  .meme-caption.bottom { bottom: 4px; }
  .post-actions {
    display: flex; align-items: center; justify-content: space-between;
    height: 89px; border-bottom: 1px solid var(--divider);
  }
  .vote-buttons { display: flex; gap: 4px; }
  .vote-buttons .btn {
    width: 66px; height: 57px; border: 1px solid var(--divider);
    display: flex; align-items: center; justify-content: center;
  }
  .share { display: flex; align-items: center; gap: 6px; color: var(--title-blue); font-size: 18px; font-weight: 600; }
  .feed .post + .post .post-title { border-top: none; margin-top: 0; }
  .media-video { height: 200px; background: #05070a; }
  .live-badge {
    position: absolute; right: 8px; top: 112px; width: 130px; height: 22px;
    background: #d71f1f; border: 2px solid #ffffff; border-radius: 3px;
    color: #fff; font-size: 14px; font-weight: 700; padding-left: 10px; line-height: 18px;
  }
  .tab-bar {
    position: absolute; left: 0; bottom: 0; width: 100%; height: 104px;
    background: var(--header-blue); display: flex;
  }
  .tab { flex: 1; display: flex; align-items: center; justify-content: center; }
  .tab.active { flex: 0 0 148px; background: var(--tab-active); }
</style>
</head>
<body>
<main class="screen">
  <div class="status-bar">
    <div class="status-left">
      <span class="signal"><i></i><i></i><i></i><i></i><i></i></span>
      <span>VOLT</span>
      <svg width="24" height="18" viewBox="0 0 24 18" fill="none" stroke="#fff" stroke-width="2.4" stroke-linecap="round"><path d="M2 6a14 14 0 0 1 20 0"/><path d="M6 10a8 8 0 0 1 12 0"/><circle cx="12" cy="14.5" r="1.6" fill="#fff" stroke="none"/></svg>
    </div>
    <span>9:25 PM</span>
    <div class="status-right"><span>100%</span><span class="battery"></span></div>
  </div>

  <header class="app-header">
    <svg class="menu" width="44" height="38" viewBox="0 0 44 38" stroke="#fff" stroke-width="3"><line x1="0" y1="3" x2="44" y2="3"/><line x1="0" y1="19" x2="44" y2="19"/><line x1="0" y1="35" x2="44" y2="35"/></svg>
    <div class="brand">JOLVO</div>
    <div class="actions">
      <svg width="42" height="42" viewBox="0 0 42 42" fill="none" stroke="#fff" stroke-width="2"><path d="M36 21a15 15 0 1 1-4.4-10.6"/><path d="M32 4v7h-7"/></svg>
      <svg width="36" height="42" viewBox="0 0 36 42" stroke="#fff" stroke-width="2.5"><line x1="18" y1="5" x2="18" y2="37"/><line x1="2" y1="21" x2="34" y2="21"/></svg>
    </div>
  </header>

  <section class="feed">
    <article class="post">
      <h2 class="post-title">Contemplative Dog!</h2>
      <div class="post-meta"><span>Points: 10,301</span><span class="comments">Comments: 40</span></div>
      <div class="media">
        <div class="media-photo" role="img" aria-label="A dog sitting on a rocky ledge looking over snowy mountains under a cloudy sky"></div>
        <p class="meme-caption top">I'M STARTING TO THINK</p>
        <p class="meme-caption bottom">HE NEVER THREW THE BALL</p>
      </div>
      <div class="post-actions">
        <div class="vote-buttons">
          <span class="btn"><svg width="24" height="24" viewBox="0 0 24 24" fill="#b9bdc1"><path d="M12 2l9 10h-5v10H8V12H3z"/></svg></span>
          <span class="btn"><svg width="24" height="24" viewBox="0 0 24 24" fill="#b9bdc1"><path d="M12 22l9-10h-5V2H8v10H3z"/></svg></span>
          <span class="btn"><svg width="28" height="24" viewBox="0 0 28 24" fill="none" stroke="#b9bdc1" stroke-width="2"><path d="M2 2h24v15H12l-5 5v-5H2z"/><line x1="7" y1="7" x2="21" y2="7"/><line x1="7" y1="12" x2="17" y2="12"/></svg></span>
        </div>
        <span class="share"><svg width="20" height="18" viewBox="0 0 20 18" fill="none" stroke="#2f5e90" stroke-width="2.6"><path d="M1 3h4l9 12h5"/><path d="M1 15h4l9-12h5"/><path d="M16 0l3 3-3 3M16 12l3 3-3 3"/></svg>SHARE</span>
      </div>
    </article>

    <article class="post">
      <h2 class="post-title">I hope they make it.</h2>
      <div class="post-meta"><span>Points: 10,301</span><span class="comments">Comments: 40</span></div>
      <div class="media">
        <div class="media-video" role="img" aria-label="Night-time live news video still of a reporter outdoors"></div>
        <span class="live-badge">LIVE</span>
      </div>
    </article>
  </section>

  <nav class="tab-bar">
    <span class="tab active"><svg width="36" height="42" viewBox="0 0 36 42" fill="#fff"><path d="M18 2c2 8 14 13 14 25a14 14 0 0 1-28 0c0-7 5-10 6-15 2 3 3 5 3 8 3-5 6-10 5-18z"/><path d="M18 24c4 4 6 7 6 10a6 6 0 0 1-12 0c0-3 3-5 6-10z" fill="#2f5e90"/></svg></span>
    <span class="tab"><svg width="50" height="48" viewBox="0 0 50 48" fill="none" stroke="#fff" stroke-width="3" stroke-linejoin="round"><path d="M25 3l6.5 14 15 1.6-11.3 10 3.3 15L25 36l-13.5 7.6 3.3-15L3.5 18.6l15-1.6z"/></svg></span>
    <span class="tab"><svg width="46" height="46" viewBox="0 0 46 46" fill="#fff"><path d="M19 2h8l1.2 6 4.6 2 5-3.5 5.6 5.6-3.5 5 2 4.6 6 1.2v8l-6 1.2-2 4.6 3.5 5-5.6 5.6-5-3.5-4.6 2L27 44h-8l-1.2-6-4.6-2-5 3.5-5.6-5.6 3.5-5-2-4.6L2 27v-8l6-1.2 2-4.6-3.5-5 5.6-5.6 5 3.5 4.6-2z"/><circle cx="23" cy="23" r="7" fill="#95c5ee"/></svg></span>
    <span class="tab"><svg width="40" height="44" viewBox="0 0 40 44" fill="#fff"><circle cx="20" cy="12" r="10"/><path d="M2 44c0-12 8-18 18-18s18 6 18 18z"/></svg></span>
  </nav>
</main>
</body>
</html>
```